Wealth management Facebook Advertisement

Hello, we are trying to capture more leads to our online booking link through Facebook advertisement. We want an attractive modern design to get more clients and catch the attention of high net-worth clients. We deal with high-net-worth retirees, business owners, farmers, and wealth transfer. We offer high-net-worth client solutions that cover Financial Planning, Retirement and Estate Planning, Investment Planning, Tax Planning, and Insurance Planning. The final design that we would be looking for is modern and eye-catching and makes the prospective clients want to click our meeting link to schedule an introductory consultation.

We are in the Wealth Management / Financial Planning industry

Our online booking link Is the following :

https://bookings.qvnfinancial-demo.net/calendar/OliverBrandtAssociatesQLPrivateWealth@qvnfinancial-demo.net/bookings/

Our current Facebook page is the following:

https://www.sociopage-demo.net/BrandtPrivateWealth

Please ask any further questions for needed information for creating design

```html
<!DOCTYPE html>
<html lang="en">
<head>
<meta charset="utf-8">
<title>QL Private Wealth Management – Protect &amp; Build Your Wealth</title>
<link rel="stylesheet" href="https://fonts.googleapis.com/css2?family=Poppins:wght@300;400;500;600;700;800;900&display=swap">
<style>
:root{
  --navy:#0b2765;
  --blue:#0a74d6;
  --ink:#2a2a2a;
  --white:#ffffff;
  --line:#9aa3b5;
}
*{box-sizing:border-box;margin:0;padding:0}
html,body{width:1200px;height:1200px;overflow:hidden;background:var(--white)}
body{font-family:"Poppins",sans-serif;color:var(--ink)}
.ad{position:relative;width:1200px;height:1200px;background:var(--white);overflow:hidden}
.abs{position:absolute}

.hero-art{left:0;top:0;width:1200px;height:600px}

.brand{left:67px;top:50px;display:flex;align-items:flex-start;gap:16px;color:var(--navy)}
.brand-mark{width:90px;height:72px;background:var(--navy);margin-top:4px}
.brand-name{font-weight:600;font-size:30px;line-height:33px;color:var(--navy)}
.firm{left:179px;top:134px;font-weight:600;font-size:30px;line-height:33px;color:var(--blue)}

.intro{left:57px;top:230px;font-weight:300;font-size:40px;line-height:46px;color:var(--ink)}
.headline{left:55px;top:332px;font-weight:900;font-size:80px;line-height:78px;letter-spacing:-1px}
.headline .accent{color:var(--blue)}
.headline .strong{color:var(--navy)}
.tagline{left:57px;top:583px;font-weight:600;font-size:39px;color:var(--ink)}

.audience{left:55px;top:654px;width:1102px;height:52px;border:1.5px solid var(--navy);display:flex;align-items:center}
.audience-label{position:absolute;left:-1px;top:-1px;height:52px;width:200px;background:var(--navy);color:var(--white);font-weight:600;font-size:22px;display:flex;align-items:center;padding-left:17px;clip-path:polygon(0 0,188px 0,178px 50%,188px 100%,0 100%)}
.audience-list{display:flex;gap:22px;margin-left:208px;list-style:none}
.audience-list li{display:flex;align-items:center;gap:9px;font-weight:500;font-size:21px;color:var(--ink)}
.tick{width:18px;height:18px;flex:none}

.band{left:0;top:889px;width:1200px;height:186px;background:var(--navy)}
.services{left:67px;top:778px;width:1071px;height:190px;background:var(--white);border-radius:0 0 22px 22px;border-left:3px solid var(--navy);display:flex}
.service{flex:1;display:flex;flex-direction:column;align-items:center;position:relative}
.service + .service::before{content:"";position:absolute;left:0;top:26px;height:130px;border-left:1.5px dotted var(--line)}
.service-icon{width:104px;height:104px;margin-top:0}
.service-name{margin-top:3px;text-align:center;font-weight:600;font-size:24px;line-height:30px;color:var(--ink)}

.offer{left:62px;top:728px;font-weight:400;font-size:30px;line-height:40px;color:var(--navy);white-space:nowrap;z-index:2}
.offer b{font-weight:800}
.offer-rule{left:848px;top:747px;width:290px;height:200px;border-top:3px solid var(--navy);border-right:3px solid var(--navy);border-top-right-radius:18px;z-index:2}

.booking{left:0;top:977px;width:1200px;text-align:center;color:var(--white)}
.booking-title{font-weight:300;font-size:36px;line-height:46px}
.booking-title b{font-weight:800}
.booking-url{font-weight:400;font-size:15.5px;margin-top:8px;letter-spacing:0.1px}

.cta{left:65px;top:1102px;font-weight:800;font-size:27px;color:var(--navy);letter-spacing:-0.5px}
.contact{display:flex;align-items:center;gap:10px;font-size:15.5px;font-weight:400;color:var(--ink);white-space:nowrap}
.contact svg{width:24px;height:24px;flex:none}
.contact-col{top:1092px;display:flex;flex-direction:column;gap:12px}
.contact-left{left:352px}
.contact-right{left:724px}
</style>
</head>
<body>
<main class="ad">

  <svg class="abs hero-art" viewBox="0 0 1200 600">
    <defs>
      <linearGradient id="photoTone" x1="0" y1="0" x2="1" y2="1">
        <stop offset="0" stop-color="#d9dde4"/>
        <stop offset="0.5" stop-color="#eef0f3"/>
        <stop offset="1" stop-color="#9aa6b8"/>
      </linearGradient>
    </defs>
    <polygon points="545,0 755,0 651,321" fill="#1b4fa3"/>
    <polygon role="img" aria-label="Photo: team hands exchanging banknotes over a desk with printed bar charts and a calculator" points="767,6 1200,6 1200,60 1045,577 584,577" fill="url(#photoTone)"/>
    <polygon points="1052,588 1171,588 1112,406" fill="#1b4fa3"/>
  </svg>

  <div class="abs brand">
    <div class="brand-mark"></div>
    <div class="brand-name">QL PRIVATE WEALTH<br>MANAGEMENT</div>
  </div>
  <div class="abs firm">OLIVER BRANDT<br>&amp; ASSOCIATES</div>

  <p class="abs intro">WE ARE IN THE FINANCIAL<br>PLANNING INDUSTRY</p>
  <h1 class="abs headline"><span class="accent">PROTECT &amp;<br>BUILD YOUR</span><br><span class="strong">WEALTH</span></h1>
  <p class="abs tagline">Financial care for high net worth families</p>

  <div class="abs audience">
    <div class="audience-label">We deal with</div>
    <ul class="audience-list">
      <li><svg class="tick" viewBox="0 0 20 20"><circle cx="10" cy="10" r="10" fill="#0a74d6"/><path d="M5.5 10.2l3 3 6-6" stroke="#fff" stroke-width="2.2" fill="none"/></svg>High-net-worth retirees</li>
      <li><svg class="tick" viewBox="0 0 20 20"><circle cx="10" cy="10" r="10" fill="#0a74d6"/><path d="M5.5 10.2l3 3 6-6" stroke="#fff" stroke-width="2.2" fill="none"/></svg>Business owners</li>
      <li><svg class="tick" viewBox="0 0 20 20"><circle cx="10" cy="10" r="10" fill="#0a74d6"/><path d="M5.5 10.2l3 3 6-6" stroke="#fff" stroke-width="2.2" fill="none"/></svg>Farmers</li>
      <li><svg class="tick" viewBox="0 0 20 20"><circle cx="10" cy="10" r="10" fill="#0a74d6"/><path d="M5.5 10.2l3 3 6-6" stroke="#fff" stroke-width="2.2" fill="none"/></svg>Wealth transfer</li>
    </ul>
  </div>

  <div class="abs band"></div>

  <section class="abs services">
    <div class="service">
      <svg class="service-icon" viewBox="0 0 106 106"><circle cx="53" cy="53" r="51" fill="#fff" stroke="#0b2765" stroke-width="2.5"/><circle cx="53" cy="53" r="42" fill="#eef1f6"/><path d="M36 40a13 10 0 0 1 26 0z" fill="#0a74d6"/><rect x="48" y="40" width="2" height="8" fill="#0b2765"/><circle cx="49" cy="62" r="12" fill="#0b2765"/><text x="49" y="67" font-size="13" fill="#fff" text-anchor="middle" font-family="Poppins,sans-serif" font-weight="700">$</text><path d="M64 46l9 3v6c0 6-4 9-9 11-5-2-9-5-9-11v-6z" fill="#fff" stroke="#0a74d6" stroke-width="2.5"/></svg>
      <p class="service-name">Financial<br>Planning</p>
    </div>
    <div class="service">
      <svg class="service-icon" viewBox="0 0 106 106"><circle cx="53" cy="53" r="51" fill="#fff" stroke="#0b2765" stroke-width="2.5"/><circle cx="53" cy="53" r="42" fill="#eef1f6"/><path d="M40 38h30v6H40z" fill="#0b2765"/><rect x="62" y="44" width="4" height="30" fill="#0b2765"/><rect x="57" y="72" width="14" height="4" fill="#0b2765"/><path d="M46 50l10 3v8c0 7-5 10-10 12-5-2-10-5-10-12v-8z" fill="#0a74d6"/><text x="46" y="66" font-size="12" fill="#fff" text-anchor="middle" font-family="Poppins,sans-serif" font-weight="700">$</text></svg>
      <p class="service-name">Retirement and<br>Estate Planning</p>
    </div>
    <div class="service">
      <svg class="service-icon" viewBox="0 0 106 106"><circle cx="53" cy="53" r="51" fill="#fff" stroke="#0b2765" stroke-width="2.5"/><circle cx="53" cy="53" r="42" fill="#eef1f6"/><path d="M46 30h14l-4 8c12 6 16 18 14 32H34c-2-14 2-26 14-32z" fill="#0b2765"/><circle cx="62" cy="60" r="12" fill="#0a74d6"/><text x="62" y="65" font-size="13" fill="#fff" text-anchor="middle" font-family="Poppins,sans-serif" font-weight="700">%</text></svg>
      <p class="service-name">Investment<br>Planning</p>
    </div>
    <div class="service">
      <svg class="service-icon" viewBox="0 0 106 106"><circle cx="53" cy="53" r="51" fill="#fff" stroke="#0b2765" stroke-width="2.5"/><circle cx="53" cy="53" r="42" fill="#eef1f6"/><path d="M32 66l16-14 8 6 16-18" stroke="#0a74d6" stroke-width="5" fill="none"/><path d="M66 36h10v10z" fill="#0a74d6"/><rect x="40" y="50" width="20" height="26" rx="2" fill="#0b2765"/><rect x="43" y="53" width="14" height="5" fill="#fff"/><rect x="43" y="61" width="4" height="4" fill="#fff"/><rect x="49" y="61" width="4" height="4" fill="#fff"/><rect x="43" y="67" width="4" height="4" fill="#fff"/><rect x="49" y="67" width="4" height="4" fill="#fff"/><circle cx="67" cy="62" r="6" fill="#0b2765"/><rect x="61" y="70" width="12" height="6" fill="#0b2765"/></svg>
      <p class="service-name">Tax<br>Planning</p>
    </div>
    <div class="service">
      <svg class="service-icon" viewBox="0 0 106 106"><circle cx="53" cy="53" r="51" fill="#fff" stroke="#0b2765" stroke-width="2.5"/><circle cx="53" cy="53" r="42" fill="#eef1f6"/><path d="M36 32h22l6 6v34H36z" fill="#0b2765"/><rect x="41" y="42" width="14" height="4" fill="#fff"/><rect x="41" y="50" width="10" height="4" fill="#fff"/><path d="M64 50l12 4v9c0 8-6 12-12 14-6-2-12-6-12-14v-9z" fill="#0a74d6" stroke="#fff" stroke-width="2"/><path d="M58 62l4 4 8-8" stroke="#fff" stroke-width="3" fill="none"/></svg>
      <p class="service-name">Insurance<br>Planning</p>
    </div>
  </section>

  <h2 class="abs offer">WE OFFER <b>HIGH-NET-WORTH CLIENT SOLUTIONS</b></h2>
  <div class="abs offer-rule"></div>

  <div class="abs booking">
    <p class="booking-title"><b>OUR ONLINE BOOKING LINK</b> IS THE FOLLOWING</p>
    <p class="booking-url">https://bookings.qvnfinancial-demo.net/calendar/OliverBrandtAssociatesQLPrivateWealth@qvnfinancial-demo.net/bookings/</p>
  </div>

  <p class="abs cta">BOOK A MEETING</p>

  <div class="abs contact-col contact-left">
    <p class="contact"><svg viewBox="0 0 24 24"><circle cx="12" cy="12" r="12" fill="#0a74d6"/><path d="M8 6l2.5 0 1 3-1.5 1.2a8 8 0 0 0 3.8 3.8L15 12.5l3 1V16c0 1-1 2-2 2A10 10 0 0 1 6 8c0-1 1-2 2-2z" fill="#fff"/></svg>(555) 014-2000</p>
    <p class="contact"><svg viewBox="0 0 24 24"><circle cx="12" cy="12" r="12" fill="#0a74d6"/><rect x="6" y="8" width="12" height="9" rx="1" fill="#fff"/><path d="M6.5 8.5l5.5 4.5 5.5-4.5" stroke="#0a74d6" stroke-width="1.4" fill="none"/></svg>Oliver.Brandt@qlprivatewealth-demo.net</p>
  </div>
  <div class="abs contact-col contact-right">
    <p class="contact"><svg viewBox="0 0 24 24"><circle cx="12" cy="12" r="12" fill="#0a74d6"/><circle cx="12" cy="12" r="6.5" fill="none" stroke="#fff" stroke-width="1.4"/><ellipse cx="12" cy="12" rx="3" ry="6.5" fill="none" stroke="#fff" stroke-width="1.2"/><path d="M5.5 12h13" stroke="#fff" stroke-width="1.2"/></svg>www.oliverbrandtassociates-demo.net</p>
    <p class="contact"><svg viewBox="0 0 24 24"><circle cx="12" cy="12" r="12" fill="#0a74d6"/></svg>www.sociopage-demo.net/BrandtPrivateWealth</p>
  </div>

</main>
</body>
</html>
```